Business Card Project for Firm Deck Hoisting

Business name is "Firm Deck Hoisting" we are a scaffolding & rigging business specialising in local and remote work for:
- scaffolding (residential, commercial, industrial)
- rigging
-man material hoists
- swing stages
- labour hire

On the back of the card I would like FDH as the symbol / logo. I have attached the logos we have had created by sketch harbour. We would like to use bold colours – preferably as the same colour scheme as the logo.

Target Market(s)

Construction business

Industry/Entity Type

Construction

Contact Information for Business Card

name: Owen Pellew
Title: Director
Phone: 0491 572 864
Address: PO BOX 3251, Brackmoor SA 5196
Email: owen@firmdeckhoisting.com.au
Website: www.firmdeckhoisting.com.au

Font styles to use
Sans Serif

Requirements
Must have
• Must use existing logo & prefering using bold colours
Nice to have
• Would be nice to have a line of dot points in what we specialise in but not essential
• Would be nice to see some designs with a slogan but not essential
Should not have
• NA

```html
<!DOCTYPE html>
<html lang="en">
<head>
<meta charset="utf-8">
<title>Firm Deck Hoisting – Business Card</title>
<link href="https://fonts.googleapis.com/css2?family=Roboto:wght@400;500;700&display=swap" rel="stylesheet">
<style>
  :root {
    --backdrop: #3b3531;
    --card: #232323;
    --white: #ffffff;
    --blue: #2a7fd4;
    --text-soft: #e8e8e8;
  }
  * { margin: 0; padding: 0; box-sizing: border-box; }
  html, body { width: 1200px; height: 716px; overflow: hidden; }
  body {
    background: var(--backdrop);
    font-family: "Roboto", Arial, sans-serif;
    position: relative;
  }
  .card {
    position: absolute;
    top: 208px;
    width: 520px;
    height: 300px;
    background: var(--card);
    border-radius: 3px;
    box-shadow: 0 10px 30px rgba(0,0,0,.45);
    overflow: hidden;
  }
  .card--contact { left: 50px; }
  .card--brand { left: 630px; }

  /* contact side */
  .contact-mark {
    position: absolute;
    left: 46px; top: 132px;
    font-size: 50px; font-weight: 700;
    color: var(--white);
    letter-spacing: 1px;
  }
  .contact-rule {
    position: absolute;
    left: 212px; top: 62px;
    width: 1px; height: 136px;
    background: var(--blue);
  }
  .contact-details {
    position: absolute;
    left: 230px; top: 60px;
    color: var(--text-soft);
    font-size: 11.5px;
    line-height: 16px;
  }
  .contact-name { color: var(--blue); font-weight: 700; font-size: 14px; line-height: 17px; }
  .contact-role { margin-bottom: 10px; }
  .contact-line { display: flex; align-items: center; gap: 6px; }
  .contact-line svg { width: 10px; height: 10px; flex: none; }

  /* brand side */
  .brand-lockup {
    position: absolute;
    left: 108px; top: 106px;
    display: flex; align-items: center;
  }
  .brand-mark {
    font-size: 46px; font-weight: 700;
    color: var(--white);
    letter-spacing: 1px;
  }
  .brand-rule {
    width: 1px; height: 64px;
    background: var(--blue);
    margin: 0 14px;
  }
  .brand-name {
    font-size: 22px; font-weight: 700;
    color: var(--white);
    line-height: 24px;
    text-transform: uppercase;
  }
  .edge-tab {
    position: absolute;
    background: var(--blue);
  }
  .edge-tab--top { right: 0; top: 26px; width: 5px; height: 26px; }
  .edge-tab--left { left: 0; top: 118px; width: 5px; height: 30px; }
  .services {
    position: absolute;
    left: 0; right: 0; bottom: 44px;
    text-align: center;
    color: var(--text-soft);
    font-size: 11px;
  }
  .services .sep { color: var(--blue); margin: 0 6px; }
</style>
</head>
<body>

<section class="card card--contact">
  <div class="contact-mark">FDH</div>
  <div class="contact-rule"></div>
  <div class="contact-details">
    <div class="contact-name">Owen Pellew</div>
    <div class="contact-role">Director</div>
    <div>PO BOX 3251, Brackmoor SA 5196</div>
    <div class="contact-line">
      <svg viewBox="0 0 10 10" aria-hidden="true"><path fill="#2a7fd4" d="M2 0.8l1.6 2-1 1a5 5 0 0 0 3.6 3.6l1-1 2 1.6-1.2 1.4C4.5 9.2.8 5.5.6 2z"/></svg>
      <span>0491 572 864</span>
    </div>
    <div class="contact-line">
      <svg viewBox="0 0 10 10" aria-hidden="true"><rect x="0.5" y="2" width="9" height="6.5" rx="1" fill="#2a7fd4"/><path d="M1 2.6l4 3 4-3" stroke="#232323" stroke-width="0.9" fill="none"/></svg>
      <span>owen@firmdeckhoisting.com.au</span>
    </div>
    <div class="contact-line">
      <svg viewBox="0 0 10 10" aria-hidden="true"><circle cx="5" cy="5" r="4.5" fill="#2a7fd4"/><path d="M0.7 5h8.6M5 0.6c-2.2 2.5-2.2 6.3 0 8.8M5 0.6c2.2 2.5 2.2 6.3 0 8.8" stroke="#232323" stroke-width="0.7" fill="none"/></svg>
      <span>www.firmdeckhoisting.com.au</span>
    </div>
  </div>
</section>

<section class="card card--brand">
  <div class="edge-tab edge-tab--top"></div>
  <div class="edge-tab edge-tab--left"></div>
  <div class="brand-lockup">
    <div class="brand-mark">FDH</div>
    <div class="brand-rule"></div>
    <div class="brand-name">Firm Deck<br>Hoisting</div>
  </div>
  <p class="services">
    Scaffolding<span class="sep">|</span>Rigging<span class="sep">|</span>Man material hoists<span class="sep">|</span>Swing stages<span class="sep">|</span>Labour hire
  </p>
</section>

</body>
</html>
```